Brightpath Letterhead

We would like a letterhead for our company. I have uploaded our logo.

Brightpath Ridge Consulting
1450 W Corliss Ave Ste 310
Linden Falls, TX 75832
833-517-2906

```html
<!DOCTYPE html>
<html lang="en">
<head>
<meta charset="utf-8">
<title>Brightpath Letterhead</title>
<link href="https://fonts.googleapis.com/css2?family=Montserrat:wght@500;700&display=swap" rel="stylesheet">
<style>
  :root {
    --backdrop: #e6e6e6;
    --paper: #f7f7f7;
    --teal-deep: #1f6673;
    --teal-mid: #2e7c86;
    --mint: #7fc4a4;
    --ink: #2b3a40;
  }
  * { margin: 0; padding: 0; box-sizing: border-box; }
  html, body {
    width: 1200px;
    height: 856px;
    overflow: hidden;
    background: var(--backdrop);
    font-family: "Montserrat", Arial, sans-serif;
  }
  .letterhead {
    position: absolute;
    left: 298px;
    top: 38px;
    width: 604px;
    height: 780px;
    background: var(--paper);
    box-shadow: 0 6px 24px rgba(0, 0, 0, 0.12);
    overflow: hidden;
  }
  .brand {
    position: absolute;
    left: 40px;
    top: 38px;
    display: flex;
    align-items: center;
    gap: 8px;
    color: var(--teal-mid);
    font-weight: 700;
    font-size: 15px;
    letter-spacing: 0.06em;
    text-transform: uppercase;
  }
  .brand-dot {
    width: 14px;
    height: 14px;
    border-radius: 50%;
    background: var(--mint);
  }
  .contact {
    position: absolute;
    left: 40px;
    bottom: 52px;
    font-size: 10.5px;
    line-height: 1.45;
    color: var(--ink);
    font-weight: 500;
  }
  .contact-name {
    color: var(--teal-deep);
    font-weight: 700;
  }
  .contact-phone {
    display: flex;
    align-items: center;
    gap: 5px;
  }
  .phone-icon { width: 11px; height: 11px; }
  .corner-motif {
    position: absolute;
    right: 0;
    bottom: 0;
    width: 170px;
    height: 110px;
    background: linear-gradient(135deg, var(--teal-mid) 0%, var(--teal-deep) 70%, var(--mint) 100%);
  }
</style>
</head>
<body>
  <main class="letterhead">
    <header class="brand">
      <span class="brand-dot"></span>
      <span class="brand-name">Brightpath Ridge Consulting</span>
    </header>

    <footer class="contact">
      <p class="contact-name">Brightpath Ridge Consulting</p>
      <p class="contact-address">1450 W Corliss Ave Ste 310, Linden Falls, TX 75832</p>
      <p class="contact-phone">
        <svg class="phone-icon" viewBox="0 0 12 12" aria-hidden="true">
          <circle cx="6" cy="6" r="6" fill="var(--teal-deep)"/>
          <path d="M4.1 3.2 L5 3 L5.5 4.4 L4.9 4.9 Q5.5 6.3 7.1 7.1 L7.6 6.5 L9 7 L8.8 7.9 Q8.5 8.6 7.6 8.5 Q4.2 7.7 3.5 4.4 Q3.4 3.5 4.1 3.2 Z" fill="#fff"/>
        </svg>
        833-517-2906
      </p>
    </footer>

    <div class="corner-motif" role="img" aria-label="Decorative interlocking ring motif in teal and mint"></div>
  </main>
</body>
</html>
```